Label design for Cargo Pants.

We need modern packaging design for men's cargo pant for a brand name Vantu. All kinds of packaging designs are welcome.

The pant is folded and packaged in a poly bag. We require a label design for the brand name Vantu. The main label will be attached by a string on the belt loop. the size of that label will 25cm in length and 10cm wide. This is the first label the customer see's when he picks up the garment. Therefore, we require an eye catching design for that. If required it could have certain information about the chino pant on the main label such as Comfort fit, Wrinkle-resistant, machine washable, luxury fabric. But, if you feel that adding the above information spoils the design of the label then it is not a must to include the above information. On the back of the label we like to include the information that this pant was manufactured in an Quarv Platinum certified green plant and hence the damage to the environment because of the plant is nill.

The second label is attached on to the waist band and the purpose of that label is to include the size of the pant such 32x32. The size of that label is 8cm in length and 4cm in width. There is no design on the back on this label it has to be blank.

Sample, is provided for what we use for our chino pant.

```html
<!DOCTYPE html>
<html lang="en">
<head>
<meta charset="utf-8">
<title>Vantu Waistband Size Label</title>
<link href="https://fonts.googleapis.com/css2?family=Black+Ops+One&display=swap" rel="stylesheet">
<style>
  :root {
    --canvas-grey: #8a8279;
    --canvas-grey-light: #9a9289;
    --canvas-grey-dark: #756d65;
    --size-orange: #e2801f;
  }
  html, body {
    margin: 0;
    padding: 0;
    width: 1200px;
    height: 2400px;
    overflow: hidden;
    background: var(--canvas-grey);
  }
  .size-label {
    position: relative;
    width: 1200px;
    height: 2400px;
    overflow: hidden;
  }
  .woven-texture {
    position: absolute;
    inset: 0;
    background: radial-gradient(ellipse at 50% 45%, var(--canvas-grey-light) 0%, var(--canvas-grey) 60%, var(--canvas-grey-dark) 100%);
  }
  .label-text {
    position: absolute;
    left: 0;
    width: 100%;
    margin: 0;
    text-align: center;
    font-family: "Black Ops One", "Stardos Stencil", sans-serif;
    color: var(--size-orange);
    line-height: 1;
    white-space: nowrap;
  }
  .measure-name {
    font-size: 176px;
    letter-spacing: 2px;
  }
  .measure-waist {
    top: 316px;
    left: 10px;
    transform: translateY(-50%) scaleY(1.3);
  }
  .measure-length {
    top: 2057px;
    left: 80px;
    font-size: 186px;
    transform: translateY(-50%) scaleY(1.15);
  }
  .size-value {
    font-size: 330px;
    letter-spacing: -6px;
    left: 40px;
  }
  .size-waist {
    top: 690px;
    transform: translateY(-50%) scaleY(1.35);
  }
  .size-length {
    top: 1551px;
    transform: translateY(-50%) scaleY(1.35);
  }
  .size-separator {
    top: 1075px;
    left: 20px;
    font-size: 190px;
    transform: translateY(-50%);
  }
</style>
</head>
<body>
  <main class="size-label">
    <div class="woven-texture" role="img" aria-label="Grey woven canvas fabric texture"></div>
    <p class="label-text measure-name measure-waist">WAIST</p>
    <p class="label-text size-value size-waist">32</p>
    <p class="label-text size-separator">x</p>
    <p class="label-text size-value size-length">32</p>
    <p class="label-text measure-name measure-length">LENGHT</p>
  </main>
</body>
</html>
```